CPA, Management and IT Consulting Redesign Existing Website

We currently have a website that is outdated (www.kelvorant.com). We need a good website developer that can redesign our website. To make this easier I have chosen a few websites that we like the layout or template. Use our exiting website content for this project. Our new logo is attached below. Based on who wins this we will upgrade to a coded website and a content management system (CMS) so we can make changes to the text ourselves in the future.

http://www.marbeckhollis.com/
http://www.quorvelmanagement.com/

Target Market(s)

Government Clients

Industry/Entity Type

Management Consulting

Number of Pages Required

5+ page

Font styles to use
Serif

Requirements
Must have
• Please the following website templates as a guide.
• http://www.marbeckhollis.com/
• http://www.quorvelmanagement.com/
Nice to have
Should not have

```html
<!DOCTYPE html>
<html lang="en">
<head>
<meta charset="utf-8">
<title>Corwell Advisory, LLC</title>
<link rel="stylesheet" href="https://fonts.googleapis.com/css2?family=Kanit:wght@300;400&family=Open+Sans:wght@400;600;700&family=Montserrat:wght@600;700&display=swap">
<style>
:root{
  --orange:#f7a03d;
  --orange-deep:#f28c1c;
  --ink:#111111;
  --text:#555555;
  --muted:#777777;
  --grey-band:#f1f1f1;
  --white:#ffffff;
  --footer:#000000;
  --navy:#1d2a4d;
}
*{box-sizing:border-box;margin:0;padding:0}
html,body{width:1200px;height:2338px;overflow:hidden}
body{position:relative;background:var(--white);font-family:"Open Sans",Arial,sans-serif;color:var(--text)}
.abs{position:absolute}
.heading{font-family:"Kanit",Arial,sans-serif;font-weight:300;color:var(--ink)}

/* top bar */
.top-bar{left:0;top:0;width:1200px;height:36px;background:var(--ink);color:#ddd;font-size:12px}
.top-bar .info{top:10px;display:flex;align-items:center;gap:7px}
.top-bar .social{top:12px;right:62px;display:flex;gap:12px}
.top-bar .social span{width:11px;height:11px;border-radius:50%;background:#fff}

/* header */
.site-header{left:0;top:36px;width:1200px;height:117px;background:var(--white)}
.brand{left:62px;top:36px;display:flex;align-items:center;gap:10px}
.brand-square{width:40px;height:48px;background:var(--orange)}
.brand-name{font-family:"Montserrat",Arial,sans-serif;font-weight:700;font-size:23px;color:var(--ink);line-height:1}
.contact-line{top:30px;display:flex;align-items:center;gap:8px;font-size:13px;color:#333}
.header-rule{left:327px;top:61px;width:812px;height:1px;background:#e4e4e4}
.btn-consult{left:982px;top:14px;width:157px;height:37px;background:var(--orange);color:#fff;font-family:"Montserrat",Arial,sans-serif;font-weight:700;font-size:11.5px;display:flex;align-items:center;justify-content:center}
.main-nav{left:329px;top:73px;display:flex;font-family:"Montserrat",Arial,sans-serif;font-weight:700;font-size:12.5px;color:var(--ink)}
.main-nav a{color:inherit;text-decoration:none;margin-right:36px}
.search-btn{left:1100px;top:68px;width:39px;height:35px;background:var(--ink);display:flex;align-items:center;justify-content:center}

/* hero */
.hero{left:0;top:153px;width:1200px;height:517px;background:linear-gradient(90deg,#8fa2b6 0%,#c9d6e2 40%,#e8eef3 60%,#b8c6d3 100%)}
.hero-caption{left:324px;top:182px;width:552px;height:142px;background:rgba(20,20,20,.88);text-align:center;color:#fff}
.hero-caption h1{font-family:"Kanit",Arial,sans-serif;font-weight:300;font-size:44px;margin-top:24px;line-height:1.1}
.hero-caption p{font-size:17px;margin-top:6px}
.hero-arrow{top:243px}

/* who we are */
.who-band{left:0;top:670px;width:1200px;height:447px;background:var(--orange)}
.who-card{left:59px;top:640px;width:1080px;height:420px;background:var(--white);text-align:center}
.who-card h2{font-size:40px;margin-top:46px}
.who-card p{width:900px;margin:26px auto 0;font-size:14px;line-height:22px;color:#444}
.partner{top:212px;width:301px;height:159px;border:1.5px solid var(--orange);display:flex;align-items:center;justify-content:center;gap:10px;font-family:"Montserrat",Arial,sans-serif;font-weight:700;font-size:20px;color:var(--ink)}
.partner .mark{width:22px;height:22px;background:var(--orange)}

/* services */
.services{left:0;top:1117px;width:1200px;height:379px;background:var(--grey-band)}
.services h2{position:absolute;top:60px;width:100%;text-align:center;font-size:40px}
.service{top:152px;width:300px;text-align:center}
.service .ring{width:118px;height:118px;margin:0 auto;border-radius:50%;border:3px solid var(--orange);display:flex;align-items:center;justify-content:center}
.service .dot{width:98px;height:98px;border-radius:50%;background:var(--orange);display:flex;align-items:center;justify-content:center}
.service h3{font-family:"Kanit",Arial,sans-serif;font-weight:400;font-size:17.5px;color:var(--ink);margin-top:20px}

/* testimonials & values */
.calc-visual{left:935px;top:1620px;width:265px;height:375px;background:linear-gradient(160deg,#ffffff 0%,#ececec 55%,#d9d9d9 100%)}
.section-title{font-size:40px}
.avatar{left:64px;top:1632px;width:118px;height:118px;border-radius:50%;background:linear-gradient(135deg,#c7ccd3,#8c95a3);border:3px solid #eee}
.quote-name{left:218px;top:1643px;font-family:"Kanit",Arial,sans-serif;font-size:18px;font-weight:400;color:var(--ink)}
.quote-role{left:218px;top:1677px;font-size:13px;color:var(--muted)}
.stars{left:218px;top:1708px;display:flex;gap:9px}
.quote-text{left:62px;top:1772px;width:378px;font-size:13px;line-height:22.5px;color:var(--muted)}
.signature{left:62px;top:1893px;width:141px;height:47px;background:linear-gradient(90deg,#e6e6e6,#f6f6f6)}
.tabs{left:503px;top:1632px;display:flex}
.tab{width:183px;height:46px;border:1px solid #ddd;display:flex;align-items:center;justify-content:center;font-family:"Kanit",Arial,sans-serif;font-size:18px;color:#333;margin-right:-1px;position:relative;background:#fff}
.tab.active{background:var(--orange);border-color:var(--orange);color:#fff}
.tab.active::after{content:"";position:absolute;bottom:-7px;left:50%;margin-left:-7px;border-left:7px solid transparent;border-right:7px solid transparent;border-top:7px solid var(--orange)}
.values-title{left:502px;top:1717px;font-family:"Open Sans",Arial,sans-serif;font-weight:700;font-size:16px;color:var(--ink)}
.values-text{left:502px;top:1746px;width:520px;font-size:13px;line-height:23px;color:var(--muted)}
.values-list{top:1852px;font-size:13px;color:#444;list-style:none}
.values-list li{display:flex;align-items:center;gap:12px;height:29.5px}

/* footer */
.site-footer{left:0;top:1995px;width:1200px;height:301px;background:var(--footer);color:#fff}
.site-footer h4{position:absolute;font-family:"Open Sans",Arial,sans-serif;font-weight:700;font-size:20px}
.footer-about{left:62px;top:84px;width:310px;font-family:Arial,sans-serif;font-size:12px;line-height:19px}
.footer-social{left:62px;top:190px;display:flex;gap:5px}
.footer-social span{width:20px;height:20px}
.footer-links{top:86px;list-style:none;font-family:Arial,sans-serif;font-size:12px;line-height:22.3px}
.footer-links li::before{content:"";display:inline-block;width:4px;height:4px;background:var(--orange);margin-right:10px;vertical-align:middle}
.field{left:940px;width:199px;background:#fff;color:#999;font-size:12px;padding:7px 9px}
.btn-send{left:941px;top:230px;width:84px;height:31px;background:var(--orange);color:#fff;font-weight:700;font-size:14px;display:flex;align-items:center;justify-content:center}
.bottom-bar{left:0;top:2296px;width:1200px;height:42px;background:#111;color:#fff;font-family:Arial,sans-serif;font-size:12.5px;display:flex;align-items:center;justify-content:center}
</style>
</head>
<body>

<div class="abs top-bar">
  <div class="abs info" style="left:59px">
    <svg width="14" height="12" viewBox="0 0 14 12"><path d="M7 0L0 6h2v6h4V8h2v4h4V6h2z" fill="#fff"/></svg>
    2180 W. Linden Ave, Arcadia
  </div>
  <div class="abs info" style="left:286px">
    <svg width="14" height="14" viewBox="0 0 14 14"><circle cx="7" cy="7" r="6" fill="none" stroke="#fff" stroke-width="1.5"/><path d="M7 3v4l3 2" stroke="#fff" stroke-width="1.5" fill="none"/></svg>
    Mon - Sat: 7:00 - 17:00
  </div>
  <div class="abs social"><span></span><span></span><span></span></div>
</div>

<header class="abs site-header">
  <div class="abs brand"><span class="brand-square"></span><span class="brand-name">CORWELL<br>ADVISORY, LLC</span></div>
  <div class="abs contact-line" style="left:327px">
    <svg width="16" height="16" viewBox="0 0 16 16"><path d="M3 1l3 3-2 2c1 2 3 4 5 5l2-2 3 3-2 3C7 15 1 9 1 3z" fill="var(--orange)"/></svg>
    (555) 204-7731
  </div>
  <div class="abs contact-line" style="left:463px">
    <svg width="20" height="14" viewBox="0 0 20 14"><rect x="1" y="1" width="18" height="12" fill="none" stroke="var(--orange)" stroke-width="1.5"/><path d="M1 1l9 7 9-7" fill="none" stroke="var(--orange)" stroke-width="1.5"/></svg>
    info@corwelladvisory.com
  </div>
  <div class="abs btn-consult">FREE CONSULTATION</div>
  <div class="abs header-rule"></div>
  <nav class="abs main-nav"><a>HOME</a><a>ABOUT US</a><a>SERVICES</a><a>INDUSTRIES</a><a>CONTACT US</a></nav>
  <div class="abs search-btn"><svg width="18" height="18" viewBox="0 0 18 18"><circle cx="7.5" cy="7.5" r="5.5" fill="none" stroke="#fff" stroke-width="2"/><path d="M11.5 11.5L16 16" stroke="#fff" stroke-width="2.2"/></svg></div>
</header>

<section class="abs hero" role="img" aria-label="Photo of two smiling consultants in a business meeting">
  <div class="abs hero-caption">
    <h1>Welcome to our company</h1>
    <p>We bring value, innovation and growth to your business</p>
  </div>
  <svg class="abs hero-arrow" style="left:20px" width="20" height="30" viewBox="0 0 20 30"><path d="M16 3L5 15l11 12" fill="none" stroke="#111" stroke-width="4"/></svg>
  <svg class="abs hero-arrow" style="left:1160px" width="20" height="30" viewBox="0 0 20 30"><path d="M4 3l11 12L4 27" fill="none" stroke="#111" stroke-width="4"/></svg>
</section>

<div class="abs who-band"></div>
<section class="abs who-card">
  <h2 class="heading">Who We Are</h2>
  <p>Corwell Advisory, LLC and Ashby &amp; Reyne, LLC is a network of certified public accounting and management consulting firms with seasoned professionals and an excellent reputation for serving a diverse client base including federal agencies, state and local government, non-profit organizations, small and medium-sized business entities, professional associations and individuals</p>
  <div class="abs partner" style="left:206px"><span class="mark"></span>Ashby &amp; Reyne</div>
  <div class="abs partner" style="left:552px"><span class="mark"></span>Corwell Advisory, LLC</div>
</section>

<section class="abs services">
  <h2 class="heading">Our Services</h2>
  <div class="abs service" style="left:14px"><div class="ring"><div class="dot">
    <svg width="40" height="44" viewBox="0 0 40 44"><rect x="8" y="4" width="24" height="32" rx="2" fill="none" stroke="#fff" stroke-width="2.5"/><path d="M13 12h14M13 18h14M13 24h10" stroke="#fff" stroke-width="2.5"/></svg>
  </div></div><h3>Accounting, Audit and Tax</h3></div>
  <div class="abs service" style="left:285px"><div class="ring"><div class="dot">
    <svg width="44" height="40" viewBox="0 0 44 40"><circle cx="16" cy="11" r="7" fill="#fff"/><path d="M4 36c0-10 6-15 12-15s12 5 12 15z" fill="#fff"/><path d="M26 30l6-7 4 4 6-8" fill="none" stroke="#fff" stroke-width="2.5"/></svg>
  </div></div><h3>Financial Management</h3></div>
  <div class="abs service" style="left:543px"><div class="ring"><div class="dot">
    <svg width="44" height="36" viewBox="0 0 44 36"><rect x="7" y="4" width="30" height="21" fill="none" stroke="#fff" stroke-width="2.5"/><path d="M3 30h38" stroke="#fff" stroke-width="3"/></svg>
  </div></div><h3>Information Technology</h3></div>
  <div class="abs service" style="left:832px"><div class="ring"><div class="dot">
    <svg width="40" height="38" viewBox="0 0 40 38"><path d="M20 2L3 11h34z" fill="#fff"/><path d="M8 14v15M16 14v15M24 14v15M32 14v15" stroke="#fff" stroke-width="3.5"/><rect x="3" y="31" width="34" height="4" fill="#fff"/></svg>
  </div></div><h3>Governance, Risk and Compliance</h3></div>
</section>

<div class="abs calc-visual" role="img" aria-label="Soft photo of a hand using a calculator beside a notebook"></div>
<h2 class="abs heading section-title" style="left:62px;top:1538px">Testimonials</h2>
<div class="abs avatar" role="img" aria-label="Portrait photo of the client"></div>
<div class="abs quote-name">Brightledger is Great Firm</div>
<div class="abs quote-role">Daniel Ortis (CEO &amp; Founder)</div>
<div class="abs stars">
  <svg width="130" height="16" viewBox="0 0 130 16"><g fill="var(--navy)"><path id="st" d="M8 0l2.4 5 5.6.8-4 3.9.9 5.5L8 12.6 3.1 15.2 4 9.7 0 5.8 5.6 5z"/><use href="#st" x="28"/><use href="#st" x="56"/><use href="#st" x="84"/><use href="#st" x="112"/></g></svg>
</div>
<p class="abs quote-text">Neque porro quisquam est, qui dolorem ipsum quia dolor sit amet, consectetur, adipis civelit sed quia non qui do-civelit sed quia numquam eius modi. Neque porro quis-quam est, qui dolorem ipsum</p>
<div class="abs signature" role="img" aria-label="Handwritten signature"></div>

<h2 class="abs heading section-title" style="left:500px;top:1538px">Our Company Values</h2>
<div class="abs tabs"><div class="tab active">Quality</div><div class="tab">Commitment</div><div class="tab">Success</div></div>
<div class="abs values-title">Our Company Quality</div>
<p class="abs values-text">Neque porro quisquam est, qui dolorem ipsum quia dolor sit amet, consectetur, quia non qui dolorem ipsum quia dolor sit amet, consectetur, adipis civelit. Red modi. Neque porro quisquam est, qui dolorem ipsum quia dolor sit amet, conse</p>
<ul class="abs values-list" style="left:503px">
  <li><svg width="15" height="15" viewBox="0 0 15 15"><circle cx="7.5" cy="7.5" r="7.5" fill="#222"/><path d="M4 7.5h6M7.5 5l2.5 2.5-2.5 2.5" stroke="#fff" stroke-width="1.5" fill="none"/></svg>Our Company Growth</li>
  <li><svg width="15" height="15" viewBox="0 0 15 15"><circle cx="7.5" cy="7.5" r="7.5" fill="#222"/><path d="M4 7.5h6M7.5 5l2.5 2.5-2.5 2.5" stroke="#fff" stroke-width="1.5" fill="none"/></svg>1000 Employed</li>
  <li><svg width="15" height="15" viewBox="0 0 15 15"><circle cx="7.5" cy="7.5" r="7.5" fill="#222"/><path d="M4 7.5h6M7.5 5l2.5 2.5-2.5 2.5" stroke="#fff" stroke-width="1.5" fill="none"/></svg>Customer Relationship</li>
</ul>
<ul class="abs values-list" style="left:743px">
  <li><svg width="15" height="15" viewBox="0 0 15 15"><circle cx="7.5" cy="7.5" r="7.5" fill="#222"/><path d="M4 7.5h6M7.5 5l2.5 2.5-2.5 2.5" stroke="#fff" stroke-width="1.5" fill="none"/></svg>Our Company Growth</li>
  <li><svg width="15" height="15" viewBox="0 0 15 15"><circle cx="7.5" cy="7.5" r="7.5" fill="#222"/><path d="M4 7.5h6M7.5 5l2.5 2.5-2.5 2.5" stroke="#fff" stroke-width="1.5" fill="none"/></svg>1000 Employed</li>
  <li><svg width="15" height="15" viewBox="0 0 15 15"><circle cx="7.5" cy="7.5" r="7.5" fill="#222"/><path d="M4 7.5h6M7.5 5l2.5 2.5-2.5 2.5" stroke="#fff" stroke-width="1.5" fill="none"/></svg>Customer Relationship</li>
</ul>

<footer class="abs site-footer">
  <h4 style="left:62px;top:42px">About Us</h4>
  <p class="abs footer-about">Aquam est tortor, sagittis in fringilla in, pellent esque nec erat. Aenean semper, neque non faucibus. tortor, sagittis in fringilla in, pellent esque nec eratsemper, neque non.Aquam est tortor, sagittis in fringilla in, pellent esque nec erat.</p>
  <div class="abs footer-social"><span style="background:#2f9fd8"></span><span style="background:#d9653b"></span><span style="background:#d6402f"></span><span style="background:#3b5798"></span></div>

  <h4 style="left:463px;top:34px">Our Services</h4>
  <ul class="abs footer-links" style="left:463px">
    <li>Website Builder</li><li>Web Design</li><li>Logo Design</li><li>Register Domains</li><li>Traffic Booster</li><li>Search Advertising</li><li>Email Marketing</li>
  </ul>

  <h4 style="left:703px;top:34px">Quick Links</h4>
  <ul class="abs footer-links" style="left:703px;top:84px">
    <li>About Hostwise</li><li>Awards Reviews</li><li>Press Media</li><li>Company Blog</li><li>Contact Us</li><li>Carrers</li>
  </ul>

  <h4 style="left:940px;top:34px">Connect With Us</h4>
  <div class="abs field" style="top:74px;height:33px">Your Name</div>
  <div class="abs field" style="top:115px;height:33px">Your Email</div>
  <div class="abs field" style="top:155px;height:66px">Message</div>
  <div class="abs btn-send">Send</div>
</footer>
<div class="abs bottom-bar">© 2016 &nbsp;Corwell Advisory All Right Reserved.</div>

</body>
</html>
```